Asian Pakistani: Wedding Invitation

Design a pakistani asian wedding invitation.
Islamic theme, with arabic text:

Text to be used:

Start with: bismillah and dua for marriage. (The Holy Quran chapter 25 verse 75 with arabic text and english translation below)

Mrs. Rukhsana Iqbal wife of (late) Mr. Nadeem Rauf Siddiqui
Cordially requests your company to grace the joyous occasion of the wedding of their beloved daughter
Sadia Siddiqui
Daughter of ( late) Mr Nadeem Rauf siddiqui
with
Imran Bashir
Son of Mr. Javed Bashir & Mrs Shaista Bashir

Insha’Allah on Thursday 29th August 2019 at Royal Orchid
12 Linden Crescent, Croydon
CR9 7TQ
Baraat Arrival 6:30

RSVP
Omar Siddiqui 07700 900412
Bilal Rehman 07700 900837
Shahzad Malik 07700 900265

Target Market(s)

Muslims

Font styles to use
Script

Colors

Designer to choose colors to be used in the design.

Requirements
Must have
• stylish calligraphy Arabic lettering of the dua requested above
• Size:
• Long 4" x 9.5"
Nice to have
• ottoman empire: Art theme

```html
<!DOCTYPE html>
<html lang="ar" dir="rtl">
<head>
<meta charset="utf-8">
<title>Wedding Invitation</title>
<link rel="stylesheet" href="https://fonts.googleapis.com/css2?family=Noto+Naskh+Arabic:wght@400;600;700&family=Amiri:wght@400;700&display=swap">
<style>
  :root {
    --page: #f4f3ef;
    --card-black: #0b0a09;
    --card-edge: #1c1a17;
    --gold: #e2bd78;
    --gold-light: #f6dea6;
    --gold-deep: #b8894a;
    --band-light: #f7e3b8;
    --band-mid: #e6c48c;
    --band-dark: #c99a5c;
    --ink: #1a1410;
  }
  * { margin: 0; padding: 0; box-sizing: border-box; }
  html, body {
    width: 1200px; height: 1098px; overflow: hidden;
    background: var(--page);
  }
  .invitation {
    position: absolute; left: 212px; top: 0;
    width: 776px; height: 1098px;
    background: radial-gradient(ellipse at 50% 40%, var(--card-edge) 0%, var(--card-black) 70%);
    font-family: "Noto Naskh Arabic", "Amiri", serif;
    color: var(--gold);
    overflow: hidden;
  }
  .lantern-garland {
    position: absolute; left: 0; top: 0; width: 776px; height: 130px;
    background: linear-gradient(180deg, rgba(226,189,120,0.35) 0%, rgba(226,189,120,0.12) 70%, rgba(226,189,120,0) 100%);
  }
  .bismillah {
    position: absolute; left: 165px; top: 150px; width: 450px; height: 120px;
    background: radial-gradient(ellipse at 55% 55%, rgba(240,204,136,0.55) 0%, rgba(184,137,74,0.25) 55%, rgba(184,137,74,0) 80%);
  }
  .dua {
    position: absolute; left: 0; top: 292px; width: 776px;
    text-align: center; font-size: 30px; font-weight: 400; line-height: 53px;
    color: var(--gold-light);
  }
  .dua .second { color: var(--gold); }
  .name-band {
    position: absolute; left: 0; top: 412px; width: 776px; height: 124px;
    border-top: 2px solid var(--gold-deep); border-bottom: 2px solid var(--gold-deep);
  }
  .name-band::before {
    content: ""; position: absolute; left: 0; right: 0; top: 6px; bottom: 6px;
    background: linear-gradient(90deg, var(--band-dark) 0%, var(--band-light) 35%, var(--band-mid) 65%, var(--band-dark) 100%);
  }
  .couple {
    position: absolute; left: 0; right: 0; top: 28px;
    text-align: center; font-size: 48px; font-weight: 700; color: var(--ink);
    line-height: 60px; white-space: nowrap;
  }
  .couple .with { font-size: 28px; margin: 0 22px; }
  .family {
    position: absolute; top: 558px; font-size: 23px; font-weight: 600; line-height: 41px;
    white-space: nowrap;
  }
  .family.groom { right: 32px; text-align: right; }
  .family.bride { right: 410px; text-align: right; }
  .family .lead { color: var(--gold-light); }
  .family-divider {
    position: absolute; left: 401px; top: 562px; width: 1px; height: 118px;
    background: var(--gold-deep);
  }
  .divider-ornament {
    position: absolute; left: 389px; top: 604px; width: 26px; height: 34px;
    background: radial-gradient(circle, var(--gold) 0%, rgba(226,189,120,0.3) 60%, rgba(0,0,0,0) 75%);
  }
  .date {
    position: absolute; left: 0; top: 704px; width: 776px; text-align: center;
    font-size: 31px; font-weight: 700; line-height: 46px; color: var(--gold-light);
  }
  .venue {
    position: absolute; left: 0; top: 802px; width: 776px; text-align: center;
    font-family: "Amiri", serif; font-size: 22px; line-height: 30px; color: var(--gold-light);
  }
  .ornament-rule {
    position: absolute; left: 265px; top: 884px; width: 246px; height: 54px;
  }
  .ornament-rule .centre {
    position: absolute; left: 88px; top: 0; width: 70px; height: 54px;
    background: radial-gradient(ellipse, var(--gold) 0%, rgba(226,189,120,0.35) 55%, rgba(0,0,0,0) 75%);
  }
  .frame-corner { position: absolute; top: 930px; left: 0; width: 776px; height: 168px; }
  .rsvp {
    position: absolute; left: 0; top: 960px; width: 776px; text-align: center;
    font-size: 15px; font-weight: 600; line-height: 21px; color: var(--gold-light);
  }
  .rsvp .num { direction: ltr; unicode-bidi: embed; }
</style>
</head>
<body>
  <main class="invitation">
    <div class="lantern-garland" role="img" aria-label="Hanging golden lanterns and stars garland"></div>
    <div class="bismillah" role="img" aria-label="Bismillah calligraphy in gold"></div>

    <p class="dua">
      <span>، أعزائنا ، امنحنا زوجاتنا وأطفالنا فرحة أعيننا</span><br>
      <span class="second">وجعلنا نموذجا من الصالحين</span>
    </p>

    <section class="name-band">
      <h1 class="couple">عمران بشير<span class="with">مع</span>سعدية صديقي</h1>
    </section>

    <div class="family groom">
      <div class="lead">عمران بشير</div>
      <div>نجل السيد جاويد بشير</div>
      <div>السيدة شائستة بشير</div>
    </div>
    <div class="family-divider"></div>
    <div class="divider-ornament" role="img" aria-label="Small gold floral ornament"></div>
    <div class="family bride">
      <div class="lead">سعدية صديقي</div>
      <div>ابنة (الراحل) السيد نديم رؤوف صديقي</div>
      <div>السيدة رخسانة إقبال</div>
    </div>

    <p class="date">إن شاء الله يوم الخميس 29 أغسطس 2019<br>بارات وصول 6:30</p>

    <p class="venue">في Royal Orchid 12 Linden Crescent ،<br>كرويدون CR9 7TQ</p>

    <div class="ornament-rule">
      <svg width="246" height="54" viewBox="0 0 246 54">
        <line x1="0" y1="27" x2="90" y2="27" stroke="#e2bd78" stroke-width="2"/>
        <line x1="156" y1="27" x2="246" y2="27" stroke="#e2bd78" stroke-width="2"/>
        <circle cx="2" cy="27" r="3" fill="#e2bd78"/>
        <circle cx="244" cy="27" r="3" fill="#e2bd78"/>
      </svg>
      <div class="centre" role="img" aria-label="Gold arabesque centre ornament"></div>
    </div>

    <svg class="frame-corner" viewBox="0 0 776 168" aria-hidden="true">
      <line x1="36" y1="10" x2="36" y2="146" stroke="#b8894a" stroke-width="1.5" stroke-dasharray="2 5"/>
      <line x1="740" y1="10" x2="740" y2="146" stroke="#b8894a" stroke-width="1.5" stroke-dasharray="2 5"/>
      <line x1="36" y1="146" x2="150" y2="146" stroke="#b8894a" stroke-width="1.5"/>
      <line x1="626" y1="146" x2="740" y2="146" stroke="#b8894a" stroke-width="1.5"/>
      <line x1="20" y1="160" x2="150" y2="160" stroke="#b8894a" stroke-width="2" stroke-dasharray="2 5"/>
      <line x1="626" y1="160" x2="756" y2="160" stroke="#b8894a" stroke-width="2" stroke-dasharray="2 5"/>
    </svg>

    <div class="rsvp">
      <div>من فضلك، أرسل رد</div>
      <div>عمر صديقي <span class="num">07700 900412</span></div>
      <div>بلال رحمن <span class="num">07700 900837</span></div>
      <div>شهزاد مالك <span class="num">07700 900265</span></div>
    </div>
  </main>
</body>
</html>
```